Crest of Morning Paddocks Business Cards with logo

Need a creative business card that pops. Colorful but professional. The attached logo should be included. We are a national horse racing partnership so we are in the equine business. Nothing cartoonlike or whimsical.

Target Market(s)

professionals - 40+

Contact Information for Business Card

Maren Dunleavy
Director of Operations
27 Ashbrook Lane
Middletown, MD. 21584

Phone (313) 555-0147

FX: (949) 555-0192

email: maren@cmpaddocks.example
cmpaddocks.example

Requirements
Must have
• All information above should be on the business card including the website address. Professional yet creative
Nice to have
• an attention grabbing design. not boring. exciting.
Should not have
• cartoon like - whimsical.

```html
<!DOCTYPE html>
<html lang="en">
<head>
<meta charset="utf-8">
<title>Crest of Morning Paddocks – Business Card</title>
<link href="https://fonts.googleapis.com/css2?family=Arimo:wght@400;700&display=swap" rel="stylesheet">
<style>
  :root {
    --backdrop: #262626;
    --card: #ffffff;
    --navy: #262c73;
    --gold: #b8902f;
    --ink: #4a4a4a;
    --rule: #6a6fa0;
  }
  * { box-sizing: border-box; margin: 0; padding: 0; }
  html, body {
    width: 1200px; height: 895px; overflow: hidden;
    background: var(--backdrop);
    font-family: "Arimo", Arial, sans-serif;
  }
  .business-card {
    position: absolute; left: 150px; top: 190px;
    width: 900px; height: 514px;
    background: var(--card);
    border-bottom: 5px solid var(--navy);
  }
  .brand {
    position: absolute; left: 60px; top: 200px;
    width: 340px;
    display: flex; align-items: center; gap: 18px;
  }
  .brand-circle {
    flex: none; width: 54px; height: 54px;
    border: 3px solid var(--gold); border-radius: 50%;
  }
  .brand-name {
    color: var(--navy); font-weight: 700;
    font-size: 26px; line-height: 1.2; letter-spacing: 0.5px;
  }
  .divider {
    position: absolute; left: 450px; top: 130px;
    width: 1.5px; height: 260px; background: var(--rule);
  }
  .contact {
    position: absolute; left: 500px; top: 130px;
    color: var(--ink);
  }
  .person-name { color: var(--navy); font-weight: 700; font-size: 34px; line-height: 1.1; }
  .person-title { font-size: 17px; margin-top: 2px; }
  .address { font-size: 15px; line-height: 1.35; margin-top: 34px; }
  .channels { list-style: none; margin-top: 30px; font-size: 16px; }
  .channels li { display: flex; align-items: center; gap: 10px; height: 22px; }
  .channels svg { width: 16px; height: 16px; fill: var(--navy); flex: none; }
</style>
</head>
<body>
  <article class="business-card">
    <div class="brand">
      <span class="brand-circle"></span>
      <span class="brand-name">Crest of Morning<br>Paddocks</span>
    </div>

    <div class="divider"></div>

    <section class="contact">
      <h1 class="person-name">Maren Dunleavy</h1>
      <p class="person-title">Director of Operations</p>
      <p class="address">27 Ashbrook Lane<br>Middletown, MD. 21584</p>
      <ul class="channels">
        <li>
          <svg viewBox="0 0 16 16" aria-hidden="true"><path d="M1 6c0-2 3-3 7-3s7 1 7 3v1h-3V5.5H4V7H1zM3 8h10l1 6H2z"/></svg>
          (313) 555-0147
        </li>
        <li>
          <svg viewBox="0 0 16 16" aria-hidden="true"><rect x="4" y="1" width="8" height="4"/><rect x="1" y="6" width="14" height="6" rx="1"/><rect x="4" y="10" width="8" height="5"/></svg>
          (949) 555-0192
        </li>
        <li>
          <svg viewBox="0 0 16 16" aria-hidden="true"><path d="M1 3h14v10H1zM2 4l6 5 6-5v1L8 10 2 5z" fill-rule="evenodd"/></svg>
          maren@cmpaddocks.example
        </li>
        <li>
          <svg viewBox="0 0 16 16" aria-hidden="true"><path d="M8 1a7 7 0 1 0 0 14A7 7 0 0 0 8 1zm0 1.5c.8.8 1.4 2.2 1.6 4H6.4C6.6 4.7 7.2 3.3 8 2.5zM2.6 7.5h2.3c.1-1.6.5-3 1.1-4a5.6 5.6 0 0 0-3.4 4zm0 1a5.6 5.6 0 0 0 3.4 4c-.6-1-1-2.4-1.1-4zm3.8 0h3.2c-.2 1.8-.8 3.2-1.6 4-.8-.8-1.4-2.2-1.6-4zm4.7 0c-.1 1.6-.5 3-1.1 4a5.6 5.6 0 0 0 3.4-4zm2.3-1A5.6 5.6 0 0 0 10 3.5c.6 1 1 2.4 1.1 4z"/></svg>
          cmpaddocks.example
        </li>
      </ul>
    </section>
  </article>
</body>
</html>
```